Business Card design for Founder and CEO of new shoe company

I am looking for a business card design for my new shoe company called Strapwell.

I am launching the company this April. Strapwell shoes offers slip-on athletic and casual style shoes for men and women. The unique selling point of the brand is that all of our shoe exist without shoelaces. I have included a link to the website to offer additional information about the company, see product images, and gain inspiration for the design. You can use the store owner password "Strapwell" to access the website.

www.Strapwell.example

Thanks,
Dan Hollis

Target Market(s)

Active Men and Women ages 16-45

Industry/Entity Type

Business

Contact Information for Business Card

Dan Hollis
Founder and CEO
www.Strapwell.example
danhollis@Strapwell.example
888-555-0187 / 888-5STRAPW
Strapwell, LLC
2284 N Tamsin Ave
Chicago, IL 60699

Requirements
Must have
• Be able to quickly and easily tell that Strapwell is a shoe company from the business card

```html
<!DOCTYPE html>
<html lang="en">
<head>
<meta charset="utf-8">
<title>Strapwell — Business Card</title>
<link rel="stylesheet" href="https://fonts.googleapis.com/css2?family=Open+Sans:wght@400;600;700&display=swap">
<style>
  :root {
    --backdrop: #3a3330;
    --card: #0b0b0b;
    --card-edge: #1c1c1c;
    --ink: #ffffff;
    --ink-soft: #d9d9d9;
    --ink-muted: #9a9a9a;
    --silver: #c9c9c9;
    --rule: #262626;
  }
  * { box-sizing: border-box; margin: 0; padding: 0; }
  html, body {
    width: 1200px; height: 900px; overflow: hidden;
    background: var(--backdrop);
    font-family: "Open Sans", sans-serif;
  }
  .stage {
    position: relative; width: 1200px; height: 900px;
    display: flex; align-items: center; justify-content: center; gap: 60px;
  }
  .card {
    position: relative;
    width: 520px; height: 297px;
    background: var(--card);
    border: 1px solid var(--card-edge);
    box-shadow: 0 14px 30px rgba(0,0,0,.45);
    overflow: hidden;
  }
  .tagline {
    font-size: 11px; font-weight: 600; letter-spacing: 3px;
    text-transform: uppercase; color: var(--ink-muted);
  }

  /* contact side */
  .card--contact .identity {
    position: absolute; left: 34px; top: 0; bottom: 0; width: 220px;
    display: flex; flex-direction: column; justify-content: center; gap: 6px;
  }
  .card--contact .brand-name {
    font-size: 36px; font-weight: 600; color: var(--ink);
    line-height: 1.1; letter-spacing: .5px;
  }
  .card--contact .divider {
    position: absolute; left: 268px; top: 60px; bottom: 60px;
    width: 1px; background: var(--rule);
  }
  .details {
    position: absolute; left: 290px; top: 40px; right: 14px;
    color: var(--ink); font-size: 13.5px; line-height: 17px;
    white-space: nowrap;
  }
  .details .person { font-weight: 700; font-size: 15px; }
  .details .role { color: var(--ink-soft); margin-bottom: 12px; }
  .details .address { color: var(--ink-soft); margin-bottom: 12px; }
  .contact-list { list-style: none; }
  .contact-list li { display: flex; align-items: center; gap: 10px; height: 19px; color: var(--ink-soft); }
  .contact-list svg { width: 11px; height: 11px; fill: var(--ink); flex: none; }

  /* brand side */
  .card--brand {
    display: flex; flex-direction: column; align-items: center; justify-content: center; gap: 8px;
  }
  .card--brand .brand-name {
    font-size: 46px; font-weight: 400; color: var(--silver);
    line-height: 1.1; letter-spacing: 1px;
  }
</style>
</head>
<body>
<main class="stage">
  <section class="card card--contact">
    <div class="identity">
      <div class="brand-name">Strapwell</div>
      <div class="tagline">Slip-on shoes</div>
    </div>
    <div class="divider"></div>
    <div class="details">
      <p class="person">Dan Hollis</p>
      <p class="role">Founder and CEO</p>
      <p class="address">Strapwell, LLC<br>2284 N Tamsin Ave<br>Chicago, IL 60699</p>
      <ul class="contact-list">
        <li><svg viewBox="0 0 12 12"><path d="M2.5 0.5 4.5 3 3.4 4.4C4.1 6 5.9 7.9 7.6 8.6L9 7.5 11.5 9.5 10.4 11.3C5.6 11 1 6.4 0.7 1.6Z"/></svg>888-555-0187</li>
        <li><svg viewBox="0 0 12 12"><path d="M2.5 0.5 4.5 3 3.4 4.4C4.1 6 5.9 7.9 7.6 8.6L9 7.5 11.5 9.5 10.4 11.3C5.6 11 1 6.4 0.7 1.6Z"/></svg>888-5STRAPW</li>
        <li><svg viewBox="0 0 12 12"><path d="M0 2h12v8H0Z M0.8 2.6 6 6.6 11.2 2.6" fill="none" stroke="#fff" stroke-width="1.2"/></svg>danhollis@Strapwell.example</li>
        <li><svg viewBox="0 0 12 12"><circle cx="6" cy="6" r="5.4"/><path d="M1 6h10M6 0.6c-2.6 3-2.6 7.8 0 10.8M6 0.6c2.6 3 2.6 7.8 0 10.8" fill="none" stroke="#0b0b0b" stroke-width=".9"/></svg>www.Strapwell.example</li>
      </ul>
    </div>
  </section>
  <section class="card card--brand">
    <div class="brand-name">Strapwell</div>
    <div class="tagline">Laceless footwear</div>
  </section>
</main>
</body>
</html>
```